Modern and Improved business card design for Family Dental Practice

We have 2 sets of logo we have designed and now just need a business card layout and design for the office. Colors are on the logo. We can choose which logo we want to go with . The font can be changed to whatever seems modern and relevant. We are family dental office that has been open for over 15 years in South Austin Texas.

Target Market(s)

Handout Business cards to referrals and specialists

Industry/Entity Type

Dental

Contact Information for Business Card

We need address, phone, website and email address. 4830 North Maple Loop Suite 208 , Austin,Texas 78392....phone: 512-847-3195.....email- info@bluepinedental.example....website - BluePineDental.example

Font styles to use
Serif
Decorative

Requirements
Must have
• my logo. We have 2 logos, but we can use just one or if we can incorporate one on one side and the other on the other side.
Nice to have
• Really just need a modern look and clean that incorporates the logo and colors .

```html
<!DOCTYPE html>
<html lang="en">
<head>
<meta charset="utf-8">
<title>Blue Pine Family Dentistry – Business Card</title>
<link rel="stylesheet" href="https://fonts.googleapis.com/css2?family=Noto+Sans:ital,wght@0,400;0,700;1,400&family=Noto+Serif:wght@700&display=swap">
<style>
  :root {
    --backdrop: #8e8e8e;
    --card-light: #e3e8d2;
    --card-mid: #c2cc93;
    --card-deep: #a1b257;
    --brand-green: #0f6b0a;
    --label-green: #0d5a10;
    --ink: #111111;
    --grey-text: #444444;
    --white: #ffffff;
  }
  html, body {
    margin: 0;
    width: 1200px;
    height: 1200px;
    overflow: hidden;
    background: var(--backdrop);
  }
  .card {
    position: absolute;
    left: 281px;
    width: 639px;
    height: 366px;
    border-radius: 22px 26px 26px 22px;
    overflow: hidden;
    font-family: "Noto Sans", sans-serif;
  }
  .card--front {
    top: 195px;
    background: linear-gradient(180deg, var(--card-light) 0%, var(--card-mid) 60%, var(--card-deep) 100%);
  }
  .card--back {
    top: 639px;
    background: var(--white);
  }
  .leaf-art {
    position: absolute;
    left: 0;
    top: 0;
    width: 280px;
    height: 366px;
    background: radial-gradient(ellipse 55% 90% at 30% 100%,
      rgba(31,122,18,0.42) 0%,
      rgba(80,130,30,0.28) 40%,
      rgba(125,140,26,0.12) 70%,
      rgba(125,140,26,0) 100%);
  }
  .holder {
    position: absolute;
    left: 319px;
    top: 78px;
    color: var(--ink);
  }
  .holder__name {
    font-family: "Noto Serif", serif;
    font-weight: 700;
    font-size: 33px;
    line-height: 1;
    margin: 0;
    letter-spacing: 0.4px;
  }
  .holder__title {
    font-size: 16px;
    letter-spacing: 0.5px;
    margin: 4px 0 0;
  }
  .holder__address {
    font-size: 15.5px;
    line-height: 19.7px;
    letter-spacing: 0.5px;
    margin: 16px 0 0;
    font-style: normal;
  }
  .contact-list {
    list-style: none;
    padding: 0;
    margin: 14px 0 0;
    font-size: 15.5px;
    line-height: 19.7px;
    letter-spacing: 0.5px;
  }
  .contact-list li {
    display: flex;
    align-items: center;
    gap: 8px;
  }
  .contact-list svg { width: 14px; height: 14px; flex: none; }
  .side-band {
    position: absolute;
    left: 0; top: 0;
    width: 19px; height: 100%;
    background: linear-gradient(180deg, var(--card-light), var(--card-mid) 60%, var(--card-deep));
  }
  .brand {
    position: absolute;
    left: 0; right: 0;
    top: 62px;
    display: flex;
    justify-content: center;
    align-items: center;
    gap: 14px;
    padding-left: 19px;
  }
  .brand__mark {
    width: 44px; height: 44px;
    border-radius: 50%;
    background: var(--brand-green);
  }
  .brand__name {
    color: var(--brand-green);
    font-size: 27px;
    font-weight: 400;
    letter-spacing: 0.5px;
  }
  .form {
    position: absolute;
    left: 56px;
    width: 528px;
    color: var(--label-green);
    font-weight: 700;
    font-size: 14.5px;
    letter-spacing: 0.5px;
  }
  .form-row {
    position: absolute;
    left: 0; right: 0;
    display: flex;
    align-items: baseline;
  }
  .form-row .fill {
    flex: 1;
    border-bottom: 1px dotted #555;
    margin: 0 1px;
    transform: translateY(-3px);
  }
  .form-row .suffix { font-size: 11.5px; }
  .row-name { top: 180px; }
  .row-date { top: 216px; }
  .days {
    position: absolute;
    top: 262px;
    left: 70px;
    right: 65px;
    display: flex;
    justify-content: space-between;
    font-size: 15px;
    font-weight: 700;
    color: var(--grey-text);
    letter-spacing: 0.6px;
  }
  .day { display: flex; align-items: center; gap: 4px; }
  .day .box {
    width: 11px; height: 11px;
    border: 1.6px solid var(--label-green);
  }
  .notice {
    position: absolute;
    top: 311px;
    left: 0; right: 0;
    text-align: center;
    font-style: italic;
    font-size: 12px;
    line-height: 13.5px;
    color: var(--grey-text);
    margin: 0;
    padding-left: 19px;
    letter-spacing: 0.6px;
  }
</style>
</head>
<body>

<section class="card card--front" aria-label="Business card front">
  <div class="leaf-art" role="img" aria-label="Tall green grass blades rising from the lower left edge"></div>
  <div class="holder">
    <h1 class="holder__name">Your Name</h1>
    <p class="holder__title">Dr Your Title</p>
    <address class="holder__address">4830 North Maple Loop<br>Suite 208<br>Austin,Texas 78392</address>
    <ul class="contact-list">
      <li>
        <svg viewBox="0 0 16 16" aria-hidden="true"><path fill="#111" d="M3.5 1.5l2.5 3-1.5 1.6c.8 1.8 2.2 3.2 4 4l1.6-1.5 3 2.5-1.6 2.4C7 13 3 9 1.5 3.5z"/></svg>
        512-847-3195
      </li>
      <li>
        <svg viewBox="0 0 16 16" aria-hidden="true"><rect x="1" y="3" width="14" height="10" fill="#111"/><path d="M1.5 3.5L8 9l6.5-5.5" fill="none" stroke="#c9d29e" stroke-width="1.2"/></svg>
        info@bluepinedental.example
      </li>
      <li>
        <svg viewBox="0 0 16 16" aria-hidden="true"><circle cx="8" cy="8" r="6.5" fill="none" stroke="#111" stroke-width="1.8"/><path d="M8 1.5v13M1.5 8h13M8 1.5c-3 3.5-3 9.5 0 13M8 1.5c3 3.5 3 9.5 0 13" fill="none" stroke="#111" stroke-width="1"/></svg>
        BluePineDental.example
      </li>
    </ul>
  </div>
</section>

<section class="card card--back" aria-label="Business card back, appointment reminder">
  <div class="side-band"></div>
  <div class="brand">
    <span class="brand__mark"></span>
    <span class="brand__name">Blue Pine Family Dentistry</span>
  </div>
  <div class="form">
    <div class="form-row row-name"><span>NAME</span><span class="fill"></span></div>
    <div class="form-row row-date"><span>DATE</span><span class="fill"></span><span>TIME</span><span class="fill"></span><span class="suffix">AM\PM</span></div>
  </div>
  <div class="days">
    <span class="day"><span class="box"></span>MON</span>
    <span class="day"><span class="box"></span>TUES</span>
    <span class="day"><span class="box"></span>WED</span>
    <span class="day"><span class="box"></span>THU</span>
    <span class="day"><span class="box"></span>FRI</span>
    <span class="day"><span class="box"></span>SAT</span>
  </div>
  <p class="notice">If you are unable to keep your appointment, please call us to<br>rescheduleatleast 48 hours prior to your appointment.</p>
</section>

</body>
</html>
```